Neues Vorlagendesign für Unternehmen aus der IT-Branche
Zielgruppe
Lindquell ist ein junges, schnell wachsendes Unternehmen in der IT-Branche aus Köln. Durch effektive Arbeitsweisen und unserem jungen, motivierten Team schaffen wir es, dass unsere Kunden mit höchster Zufriedenheit Server & Storage Systeme bei uns beziehen. Unser Fokus liegt dabei auf einer erstklassigen Beratung & schnellen Lieferzeiten.
Wir wollen es mit dem neuen Vorlagendesign schaffen, dem Kunden alle relevanten Informationen in einer strukturierten, übersichtlichen und dennoch ansprechenden Art & Weise zu überbringen.
Aufgabenstellung
Wir suchen lediglich nach dem Design der Vorlage! Ein pdf. oder ähnliches reicht!
Logo, Rechnungsadresse (Brieffenster), Rechnungsnr., Rechnungsdatum, Auftragsnr., Kundennr., Zahlungsart, Lieferungen, Auftragspositionen, Lieferadresse, Fußzeile mit Kontakt & rechtlichen infos
--> Wir möchten mit einem einfach Design dennoch eine übersichtliche & ansprechende Vorlage erstellen - eventuell könnte man hier das 'Golden Ratio' miteinbeziehen, um die Proportionen festzulegen. (A4 Format)
Die angehängte Vorlage dient lediglich als Beispiel für die benltigten Information und der 'groben' Anordnung. Wir wollen nicht ein einfaches Verändern der Vorlage durch den Auftrag vergeben!

```html
<!DOCTYPE html>
<html lang="de">
<head>
<meta charset="utf-8">
<title>Rechnung – Lindquell GmbH</title>
<link href="https://fonts.googleapis.com/css2?family=PT+Sans:wght@400;700&family=PT+Sans+Narrow:wght@400;700&family=Lato:wght@700;900&display=swap" rel="stylesheet">
<style>
:root{
  --dark:#3a3a3a;
  --orange:#f7ac45;
  --orange-soft:#fbd6a3;
  --grey-1:#e9e9e9;
  --grey-2:#f4f4f4;
  --text:#1e1e1e;
  --paper:#ffffff;
}
*{margin:0;padding:0;box-sizing:border-box}
html,body{width:847px;height:1200px;overflow:hidden;background:var(--paper)}
body{font-family:"PT Sans",sans-serif;color:var(--text);position:relative}
.abs{position:absolute}
.header-shape{left:0;top:0}
.brand{left:152px;top:36px;color:#e8e8e8}
.brand-name{font-family:"Lato",sans-serif;font-weight:700;font-size:30px;letter-spacing:1.5px;line-height:1}
.brand-sub{position:absolute;left:115px;top:33px;font-size:11px;color:#e8e8e8;white-space:nowrap}
.window{left:86px;top:174px;width:345px;height:166px}
.sender{left:150px;top:192px;font-size:8.5px;font-weight:700;border-bottom:1px solid #aaa;padding-bottom:1px}
.recipient{left:113px;top:238px;font-size:13px;line-height:16.5px}
.doc-title{left:89px;top:357px;font-size:20px}
.delivery{left:89px;top:383px;font-size:10.5px;font-family:"PT Sans Narrow",sans-serif;line-height:12.6px}
.delivery span{position:absolute;left:86px;top:0;white-space:nowrap}
.info{left:464px;top:172px;width:312px;height:264px;background:var(--orange-soft)}
.info-row{position:absolute;left:0;height:29px;width:312px;font-family:"PT Sans Narrow",sans-serif;font-size:9.5px;font-weight:700}
.info-row .lbl{position:absolute;left:6px;top:9px}
.info-row .val{position:absolute;top:5px;height:20px;background:#fff;border:1px solid #d9c3a0;padding:4px 7px;white-space:nowrap}
.fold{left:18px;width:0;height:0;border-top:4px solid transparent;border-bottom:4px solid transparent;border-left:5px solid var(--dark)}
.items{left:67px;top:511px;width:712px;height:488px;border:1px solid #8c8c8c;background:#fff}
.items-head{position:absolute;left:0;top:0;width:710px;height:26px;background:var(--orange);color:#fff;font-family:"PT Sans Narrow",sans-serif;font-weight:700;font-size:11.5px}
.items-head span,.row span{position:absolute;white-space:nowrap}
.items-head span{top:5px}
.group{position:absolute;left:0;width:710px}
.row{position:absolute;left:0;width:710px;font-family:"PT Sans Narrow",sans-serif;font-size:12.5px;line-height:16.5px}
.summary-note{position:absolute;font-family:Arial,sans-serif;font-size:5.6px;line-height:6.6px}
.totals{position:absolute;font-family:"Lato",sans-serif;font-weight:700;font-size:13px}
.total-due{position:absolute;left:320px;top:454px;width:391px;height:33px;background:var(--orange);color:#fff;font-family:"Lato",sans-serif;font-weight:900}
.footer-line{left:0;top:1106px;width:847px;height:6px;background:var(--orange)}
.footer-mark{left:684px;top:1099px;width:76px;height:22px;background:#fff;text-align:center;font-size:14px;font-weight:700;color:var(--dark);line-height:22px}
.legal{left:86px;top:1119px;font-size:10.5px;line-height:13px}
.postal{left:350px;top:1119px;font-size:10.5px;line-height:13px}
.contact{left:463px;top:1137px;font-size:10.5px;line-height:21px}
.ico{position:absolute}
.web{left:661px;top:1160px;color:#e5e5e5;font-size:13px;font-weight:700}
</style>
</head>
<body>

<svg class="abs header-shape" width="847" height="100" viewBox="0 0 847 100" aria-hidden="true">
  <polygon points="0,0 847,0 847,68 392,68 372,96 0,96" fill="#3a3a3a"/>
  <polygon points="392,78 847,78 847,84 388,84" fill="#f7ac45"/>
  <polygon points="382,91 847,91 847,97 378,97" fill="#f7ac45"/>
</svg>

<div class="abs brand">
  <div class="brand-name">LINDQUELL</div>
  <div class="brand-sub">Lindquell GmbH</div>
</div>

<svg class="abs window" viewBox="0 0 345 166" aria-hidden="true">
  <path d="M1,28 V14 Q1,1 14,1 H28" fill="none" stroke="#555" stroke-width="1"/>
  <path d="M316,1 H330 Q343,1 343,14 V28" fill="none" stroke="#555" stroke-width="1"/>
  <path d="M1,138 V152 Q1,165 14,165 H28" fill="none" stroke="#555" stroke-width="1"/>
  <path d="M316,165 H330 Q343,165 343,152 V138" fill="none" stroke="#555" stroke-width="1"/>
</svg>
<div class="abs sender">Lindquell GmbH - Kranweg 14 - D-50829 Köln</div>
<div class="abs recipient">Herr.:<br>Anton Berwald<br>Web Master<br>City</div>

<div class="abs doc-title">Rechnung</div>
<div class="abs delivery">Lieferanschrift:
  <span>Lea Sommer Lindquell<br>Frau Lea Sommer<br>Lindenhof 7<br>52062 Aachen<br>Deutschland</span>
</div>

<div class="abs info">
  <div class="info-row" style="top:1px"><span class="lbl">Rechnungs Nr:</span><span class="val" style="left:90px;width:56px">R15455</span><span class="lbl" style="left:152px">Rechnungs Datum</span><span class="val" style="left:234px;width:70px">11.03.2020</span></div>
  <div class="info-row" style="top:30px"><span class="lbl">Auftragsnummer</span><span class="val" style="left:90px;width:56px">504582</span><span class="lbl" style="left:159px">Ihr Bestelldatum</span><span class="val" style="left:234px;width:70px">10.03.2020</span></div>
  <div class="info-row" style="top:59px"><span class="lbl">Kunden-Nummer</span><span class="val" style="left:90px;width:56px">5265</span><span class="lbl" style="left:205px">Seite</span><span class="val" style="left:234px;width:70px">1 von 2</span></div>
  <div class="info-row" style="top:88px"><span class="lbl">Zahlungsart:</span><span class="val" style="left:90px;width:214px">Rechnung 10 Tage (Kein Factoring)</span></div>
  <div class="info-row" style="top:117px"><span class="lbl">Versandart:</span><span class="val" style="left:90px;width:214px">Test2</span></div>
  <div class="info-row" style="top:147px"><span class="lbl">Bestellt durch:</span><span class="val" style="left:90px;width:214px">Lea Sommer</span></div>
  <div class="info-row" style="top:176px"><span class="lbl">Bearbeiter:</span><span class="val" style="left:90px;width:214px">Jonas Weyer</span></div>
  <div class="info-row" style="top:205px"><span class="lbl">Bearbeiter Tel:</span><span class="val" style="left:90px;width:214px">+49 (0) 221 5550 237</span></div>
  <div class="info-row" style="top:235px"><span class="lbl">Bearbeiter Mail:</span><span class="val" style="left:90px;width:214px">j.weyer@lindquell.de</span></div>
</div>

<div class="abs fold" style="top:458px"></div>
<div class="abs fold" style="top:767px"></div>

<div class="abs items">
  <div class="items-head">
    <span style="left:21px">Pos</span><span style="left:64px">Menge</span><span style="left:120px">Art. Nr.</span><span style="left:198px">Bezeichnung</span><span style="left:503px">MwSt</span><span style="left:560px">E-Preis</span><span style="left:613px">Gesamt Netto</span>
  </div>
  <div class="group" style="top:26px;height:110px;background:var(--grey-1)"></div>
  <div class="group" style="top:136px;height:111px;background:var(--grey-2)"></div>
  <div class="group" style="top:247px;height:110px;background:var(--grey-1)"></div>

  <div class="row" style="top:40px"><span style="left:27px">1</span><span style="left:73px">1</span><span style="left:119px">3000062</span><span style="left:197px">RX R360 Mk9 1xQX-2600c 1x16GB 8xSFF DVD<br>&nbsp;C440r/2G 1x500W Rack Server</span><span style="left:504px">19,00</span><span style="left:570px">0,00</span><span style="left:643px">0,00</span></div>
  <div class="row" style="top:82px"><span style="left:27px">2</span><span style="left:66px">1</span><span style="left:199px;letter-spacing:1px">Test2</span><span style="left:504px">19,00</span><span style="left:570px">0,00</span><span style="left:643px">0,00</span></div>
  <div class="row" style="top:169px"><span style="left:27px">1</span><span style="left:73px">1</span><span style="left:119px">3000062</span><span style="left:197px">RX R360 Mk9 1xQX-2600c 1x16GB 8xSFF DVD<br>&nbsp;C440r/2G 1x500W Rack Server</span><span style="left:504px">19,00</span><span style="left:570px">0,00</span><span style="left:643px">0,00</span></div>
  <div class="row" style="top:211px"><span style="left:27px">2</span><span style="left:66px">1</span><span style="left:199px;letter-spacing:1px">Test2</span><span style="left:504px">19,00</span><span style="left:570px">0,00</span><span style="left:643px">0,00</span></div>

  <div class="summary-note" style="left:11px;top:375px">Zahlungshinweis</div>
  <div class="summary-note" style="left:110px;top:375px;width:205px">Wir bitten Sie den fälligen Betrag auf folgende Bankverbindung zu überweisen:<br><br>Lindquell GmbH<br>IBAN: DE00 1234 5678 9012 3456 78<br>BIC: STBKDE33XXX<br>Bank: Stadtbank Aachen<br>Verwendungszweck: R15455</div>
  <div class="summary-note" style="left:16px;top:452px">Anmerkungen</div>
  <div class="summary-note" style="left:112px;top:452px">Vielen Dank für Ihren Auftrag.</div>

  <div class="totals" style="left:376px;top:372px">Gesamtpreis Netto</div>
  <div class="totals" style="left:625px;top:372px">0,02 EUR</div>
  <div class="totals" style="left:376px;top:397px">MwSt. 19,00%</div>
  <div class="totals" style="left:625px;top:397px">0,00 EUR</div>
  <div class="totals" style="left:376px;top:425px">Gesamtpreis Brutto</div>
  <div class="totals" style="left:625px;top:425px">0,02 EUR</div>
  <div class="total-due">
    <span style="position:absolute;left:56px;top:6px;font-size:17px">TOTAL DUE</span>
    <span style="position:absolute;left:285px;top:6px;font-size:16px">70,00</span>
    <span style="position:absolute;left:340px;top:9px;font-size:12px">EUR</span>
  </div>
</div>

<div class="abs footer-line"></div>
<div class="abs footer-mark">Lindquell</div>

<svg class="abs" style="left:0;top:1132px" width="847" height="68" viewBox="0 0 847 68" aria-hidden="true">
  <polygon points="583,0 847,0 847,68 0,68 0,55 566,55" fill="#3a3a3a"/>
</svg>

<svg class="abs ico" style="left:58px;top:1146px" width="14" height="13" viewBox="0 0 14 13" aria-hidden="true">
  <polygon points="7,0 14,4 0,4" fill="#f7ac45"/><rect x="2" y="5" width="2" height="6" fill="#f7ac45"/><rect x="6" y="5" width="2" height="6" fill="#f7ac45"/><rect x="10" y="5" width="2" height="6" fill="#f7ac45"/><rect x="0" y="11" width="14" height="2" fill="#f7ac45"/>
</svg>
<div class="abs legal">Steuernummer: 215/4402/0117<br>Amtsgericht Köln HRB 10458<br>Ust.Id.:DE300451928<br>Geschäftsführer: Milan Ostrow, Paul Renner</div>

<svg class="abs ico" style="left:330px;top:1146px" width="16" height="16" viewBox="0 0 16 16" aria-hidden="true">
  <polygon points="0,2 16,8 0,15 4,8" fill="#f7ac45"/>
</svg>
<div class="abs postal">Lindquell GmbH<br>Kranweg 14<br>D-50829 Köln<br>Deutschland</div>

<svg class="abs ico" style="left:448px;top:1142px" width="11" height="11" viewBox="0 0 11 11" aria-hidden="true">
  <path d="M2,0 L4,3 L3,4 Q4,7 7,8 L8,7 L11,9 L9,11 Q1,10 0,2 Z" fill="#f7ac45"/>
</svg>
<svg class="abs ico" style="left:447px;top:1164px" width="12" height="9" viewBox="0 0 12 9" aria-hidden="true">
  <rect x="0.5" y="0.5" width="11" height="8" fill="none" stroke="#f7ac45"/><path d="M0.5,0.5 L6,5 L11.5,0.5" fill="none" stroke="#f7ac45"/>
</svg>
<div class="abs contact">+49 221 5550 500<br>info@lindquell.de</div>

<svg class="abs ico" style="left:639px;top:1162px" width="14" height="14" viewBox="0 0 14 14" aria-hidden="true">
  <g fill="none" stroke="#e5e5e5" stroke-width="1"><circle cx="7" cy="7" r="6"/><ellipse cx="7" cy="7" rx="2.6" ry="6"/><path d="M1,7 H13 M2,4 H12 M2,10 H12"/></g>
</svg>
<div class="abs web">www.lindquell.de</div>

</body>
</html>
```